Brindle Hub is an online marketing platform

A daily deals site for consumers a way to bring in new clients for clients and this is who the business cards are for. Industries - Food and Drink, Things To Do, Beauty and Spas, Staycations and Services.This leaflet is going to be used to get member of the public to sign up to our website

```html
<!DOCTYPE html>
<html lang="en">
<head>
<meta charset="utf-8">
<title>Brindle Hub – Launch Leaflet</title>
<link rel="stylesheet" href="https://fonts.googleapis.com/css2?family=Open+Sans:wdth,wght@75..100,300..800&display=swap">
<style>
  :root {
    --brand-blue: #0d5cb6;
    --brand-blue-deep: #0a4f9f;
    --ink: #1a1a1a;
    --charcoal: #4a4a4a;
    --form-grey: #7a7a7a;
    --paper: #ffffff;
    --backdrop: #ece9e4;
    --photo-light: #eef0f2;
    --photo-mid: #c9ced4;
  }
  * { box-sizing: border-box; margin: 0; padding: 0; }
  html, body { width: 1200px; height: 886px; overflow: hidden; }
  body {
    background: var(--backdrop);
    font-family: "Open Sans", Arial, sans-serif;
    color: var(--ink);
  }
  .leaflet {
    position: absolute; left: 300px; top: 18px;
    width: 600px; height: 850px;
    background: var(--paper);
    overflow: hidden;
  }

  /* Header */
  .brand-name {
    position: absolute; left: 28px; top: 34px;
    font-size: 48px; font-weight: 700; line-height: 1;
    color: var(--brand-blue); letter-spacing: 0.5px;
  }
  .launch-box {
    position: absolute; right: 0; top: 0; z-index: 2;
    width: 161px; height: 140px;
    background: var(--charcoal);
    border-bottom-left-radius: 20px;
    color: #fff; padding: 12px 12px 0 14px;
  }
  .launch-title {
    font-size: 19px; font-weight: 700; font-stretch: 80%; line-height: 1.3;
  }
  .launch-title sup { font-size: 10px; }
  .launch-note {
    margin-top: 5px; font-size: 12.5px; line-height: 1.4; text-align: justify;
  }

  /* Hero band */
  .hero-panel {
    position: absolute; left: 0; top: 126px;
    width: 282px; height: 266px;
    background: var(--brand-blue);
    color: #fff; text-align: center;
    padding-top: 70px;
  }
  .hero-kicker { font-size: 15.5px; }
  .hero-cta { font-size: 17px; font-weight: 700; margin-top: 6px; }
  .hero-url {
    display: inline-block; margin-top: 5px;
    border: 1px solid rgba(255,255,255,0.8); border-radius: 8px;
    padding: 1px 18px; font-size: 15px; font-weight: 700;
  }
  .hero-copy {
    margin: 12px auto 0; width: 226px;
    font-size: 15px; line-height: 1.4;
  }
  .hero-copy strong { font-weight: 700; }
  .hero-photo {
    position: absolute; left: 282px; top: 126px;
    width: 318px; height: 266px;
    background: linear-gradient(160deg, var(--photo-light) 0%, var(--photo-mid) 100%);
  }

  /* Prize banner */
  .prize-banner {
    position: absolute; left: 24px; top: 400px;
    width: 550px; height: 89px;
    background: #000; border-radius: 30px;
    color: #fff; text-align: center; padding-top: 6px;
  }
  .prize-headline { font-size: 33px; font-weight: 700; font-stretch: 88%; line-height: 1.15; word-spacing: 3px; }
  .prize-sub { font-size: 23px; font-weight: 300; font-stretch: 75%; line-height: 1.3; }
  .intro {
    position: absolute; left: 40px; top: 505px; width: 520px;
    font-size: 11.5px; line-height: 1.55; text-align: center; color: var(--ink);
  }

  /* Entry form */
  .entry-form {
    position: absolute; left: 0; top: 552px;
    width: 600px; height: 256px;
    background: var(--form-grey);
    padding: 4px;
  }
  .entry-inner {
    width: 100%; height: 100%;
    border: 1px dashed rgba(0,0,0,0.45);
    padding: 10px 22px 0 22px;
  }
  .entry-heading { font-size: 15px; font-weight: 700; line-height: 1.4; color: var(--ink); width: 520px; }
  .entry-field { display: flex; align-items: flex-end; margin-top: 12px; font-size: 15px; font-weight: 700; }
  .entry-field:first-of-type { margin-top: 14px; }
  .entry-field span { width: 74px; }
  .entry-line { flex: 1; border-bottom: 1px solid var(--ink); margin-bottom: 4px; margin-right: 22px; }
  .entry-optout { margin-top: 14px; font-size: 10.5px; color: var(--ink); }

  /* Footer */
  .follow-bar {
    position: absolute; left: 0; bottom: 0;
    width: 600px; height: 40px;
    background: var(--brand-blue-deep);
    color: #fff; display: flex; align-items: center; justify-content: center; gap: 8px;
    font-size: 18px; font-weight: 600;
  }
  .social-dot { width: 15px; height: 15px; border-radius: 50%; background: #fff; }
</style>
</head>
<body>
  <article class="leaflet">
    <header>
      <div class="brand-name">Brindle Hub</div>
      <aside class="launch-box">
        <div class="launch-title">LAUNCHING ON<br>1<sup>ST</sup> AUGUST 2019</div>
        <p class="launch-note">Be the first to receive exclusive offers and WIN!</p>
      </aside>
    </header>

    <section class="hero-panel">
      <p class="hero-kicker">Pretty Cool?</p>
      <p class="hero-cta">REGISTER FOR FREE NOW AT</p>
      <p class="hero-url">brindlehub.co.uk</p>
      <p class="hero-copy">Find inspiration for places to <strong>EAT</strong>, things to <strong>DO</strong> and where to get a <strong>PAMPER.</strong></p>
    </section>
    <div class="hero-photo" role="img" aria-label="Laptop and tablet showing the Brindle Hub website on a bright desk"></div>

    <section class="prize-banner">
      <p class="prize-headline">HEY YOU!&nbsp; WANT TO WIN £200</p>
      <p class="prize-sub">To Spend On The Best Experiences The South West Has To Offer?</p>
    </section>
    <p class="intro">Brindle Hub is a brand spanking new website that gives you access to exciting offers across the best restaurants, hotels, spas, leisure activities and services.</p>

    <section class="entry-form">
      <div class="entry-inner">
        <p class="entry-heading">Complete Your Details Below For Your Chance To Win And Be The First To Receive Fresh Fancy Offers Just For You.</p>
        <div class="entry-field"><span>Name:</span><div class="entry-line"></div></div>
        <div class="entry-field"><span>Email:</span><div class="entry-line"></div></div>
        <div class="entry-field"><span>Mobile:</span><div class="entry-line"></div></div>
        <div class="entry-field"><span>Address:</span><div class="entry-line"></div></div>
        <p class="entry-optout">( ) Please tick here if you would not like to receive updates on fabulous offers and new experiences.</p>
      </div>
    </section>

    <footer class="follow-bar">
      Follow Us-
      <span class="social-dot"></span>
      <span class="social-dot"></span>
      <span class="social-dot"></span>
    </footer>
  </article>
</body>
</html>
```